Business card required for IT Consultancy Business - Tealbrook Consulting.
Company provides the whole nine yards of services across IT Architecture, design and execution.
Basically we provide consulting services to help businesses make sure their technology is enabling their business strategy.
Design for front and back required.
We would like the front of the card to inlcude:
Name
Title
Mobile number
email address
www.tbkc.com.au
Company logos attached.
Thank you
Industry/Entity Type
Business
Contact Information for Business Card
Name
Title
Mobile number
email address
www.tbkc.com.au
Look and feel
Each slider illustrates characteristics of the customer's brand and the style your logo design should communicate.

```html
<!DOCTYPE html>
<html lang="en">
<head>
<meta charset="utf-8">
<title>Tealbrook Consulting – Business Card</title>
<link href="https://fonts.googleapis.com/css2?family=Lato:wght@400;700;900&display=swap" rel="stylesheet">
<style>
  :root {
    --brand-orange: #ef5a2a;
    --brand-blue: #1273c1;
    --card-white: #f8f8f8;
    --text-grey: #7a7a7a;
    --page-bg: #ececec;
    --white: #ffffff;
  }
  * { margin: 0; padding: 0; box-sizing: border-box; }
  html, body {
    width: 1200px; height: 586px; overflow: hidden;
    background: var(--page-bg);
    font-family: "Lato", Arial, sans-serif;
  }
  .canvas { position: relative; width: 1200px; height: 586px; }
  .card {
    position: absolute; top: 129px;
    width: 502px; height: 301px; overflow: hidden;
  }
  .card--back { left: 61px; background: var(--brand-orange); }
  .card--front { left: 619px; background: var(--card-white); }

  .back-wordmark {
    position: absolute; left: 0; right: 0; top: 112px;
    text-align: center; color: var(--white);
    font-weight: 900; font-size: 38px; letter-spacing: 0.5px;
  }
  .back-website {
    position: absolute; left: 0; right: 0; top: 246px;
    text-align: center; color: var(--white);
    font-weight: 700; font-size: 12px; letter-spacing: 4.5px;
  }

  .front-wordmark {
    position: absolute; left: 0; right: 0; top: 50px;
    text-align: center; color: var(--brand-blue);
    font-weight: 900; font-size: 27px;
  }
  .holder {
    position: absolute; right: 292px; top: 178px; text-align: right;
  }
  .holder__name {
    color: var(--brand-orange); font-weight: 900; font-size: 13.5px;
  }
  .holder__title {
    margin-top: 4px; color: var(--text-grey); font-size: 11px;
  }
  .divider {
    position: absolute; left: 243px; top: 143px; width: 2px; height: 105px;
    background: linear-gradient(to bottom, rgba(18,115,193,0), var(--brand-blue) 50%, rgba(18,115,193,0));
  }
  .contact {
    position: absolute; left: 276px; top: 149px;
  }
  .contact__row {
    display: flex; align-items: center; height: 24px;
    color: var(--text-grey); font-size: 12px;
  }
  .contact__icon { width: 17px; height: 17px; margin-right: 7px; flex: none; }
  .contact__address {
    margin-top: 6px; color: var(--brand-orange);
    font-weight: 700; font-size: 12px; line-height: 24px;
  }
  .front-bands { position: absolute; left: 0; bottom: 0; }
</style>
</head>
<body>
<div class="canvas">

  <section class="card card--back" aria-label="Card back">
    <div class="back-wordmark">Tealbrook Consulting</div>
    <div class="back-website">www.tbkc.com.au</div>
  </section>

  <section class="card card--front" aria-label="Card front">
    <div class="front-wordmark">Tealbrook Consulting</div>

    <div class="holder">
      <div class="holder__name">MARISOL OKAFOR</div>
      <div class="holder__title">Owner &amp; Founder</div>
    </div>

    <div class="divider"></div>

    <div class="contact">
      <div class="contact__row">
        <svg class="contact__icon" viewBox="0 0 20 20" aria-hidden="true">
          <circle cx="10" cy="10" r="10" fill="#ef5a2a"/>
          <path d="M5 8.5c0-1.5 2.2-2.5 5-2.5s5 1 5 2.5v1h-2.6V8.3H7.6v1.2H5z M6.5 14l1.5-3.5h4l1.5 3.5z" fill="#fff"/>
        </svg>
        (555) 214-3096
      </div>
      <div class="contact__row">
        <svg class="contact__icon" viewBox="0 0 20 20" aria-hidden="true">
          <circle cx="10" cy="10" r="10" fill="#ef5a2a"/>
          <rect x="5" y="6.5" width="10" height="7" fill="none" stroke="#fff" stroke-width="1.3"/>
          <path d="M5 6.5l5 4 5-4" fill="none" stroke="#fff" stroke-width="1.3"/>
        </svg>
        marisol@tealbrookconsult.com
      </div>
      <div class="contact__address">
        412 Harbor Lane, Suite 210,<br>
        Bayview Heights, CA 90410
      </div>
    </div>

    <svg class="front-bands" width="502" height="16" viewBox="0 0 502 16" aria-hidden="true">
      <rect x="0" y="4" width="312" height="12" fill="#1273c1"/>
      <path d="M304 16 C306 6 312 0 324 0 H502 V16 Z" fill="#ffffff"/>
      <path d="M310 16 C312 7 318 2 330 2 H502 V16 Z" fill="#ef5a2a"/>
    </svg>
  </section>

</div>
</body>
</html>
```